Purrline Fest Ticket Card Design

We’re looking to create a complimentary “ticket” card for Purrline Fest that can be handed out physically. We host an event for cat lovers. The card should feel special and collectible. Size will be a standard business card (3.5" x 2") Orientation is open to designer recommendation. This ticket will be used as a complimentary entry pass for select guests, partners, & giveaways. Key elements to Include are the Purrline Fest logo (provided), the words “Complimentary Ticket” or similar wording (open to creative phrasing and cat puns) A blank space for the Event date (to be written in) & Ticket number (to be written in) . Event Name is always "Purrline Bazaar & Rescue Gala". We want the ticket to feel clean & modern but slightly playful with a cat-inspired touch (think clever, not kitschy). Could include a subtle cat motif or texture (e.g., whisker lines, paw detail, soft patterning) Open to unique layout ideas that still leave clear writing space. Avoid overcrowding of elements. Ticket should also have fine print "This ticket is not redeemable for cash and cannot be combined with any other offers or discounts, can only be used for the date indicated"

Target Market(s)

Women

Industry/Entity Type

pets

Colors
6B429C
8869AF
B7A5CE
E3DAEB
F3F0F8

Requirements
Must have
• Purrline Fest Logo & words around complimentary ticket as well as the fine print
Nice to have
• cat-inspired touch (think clever, not kitschy). Could include a subtle cat motif or texture (e.g., whisker lines, paw detail, soft patterning)
Should not have
• should not look cartoony

```html
<!DOCTYPE html>
<html lang="en">
<head>
<meta charset="utf-8">
<title>Purrline Fest – Complimentary Ticket Card</title>
<link rel="stylesheet" href="https://fonts.googleapis.com/css2?family=Poppins:ital,wght@0,400;0,500;0,600;1,400&family=Fredoka:wght@700&display=swap">
<style>
  :root {
    --purple-deep: #6B429C;
    --purple-mid: #8869AF;
    --purple-soft: #B7A5CE;
    --lilac: #E3DAEB;
    --mist: #F3F0F8;
    --white: #FFFFFF;
  }
  * { margin: 0; padding: 0; box-sizing: border-box; }
  html, body {
    width: 1024px;
    height: 1200px;
    overflow: hidden;
    background: var(--white);
    font-family: "Poppins", sans-serif;
  }
  .sheet { position: relative; width: 1024px; height: 1200px; }
  .side-label {
    position: absolute;
    left: 0; width: 1024px;
    text-align: center;
    color: var(--purple-deep);
    font-size: 27px;
    font-weight: 500;
    letter-spacing: 1.5px;
  }
  .side-label--front { top: 36px; }
  .side-label--back { top: 1119px; }

  .card { position: absolute; left: 119px; }
  .card--front {
    top: 122px; width: 784px; height: 448px;
    background: var(--purple-deep);
  }
  .card--back {
    top: 626px; width: 778px; height: 445px;
    background: var(--mist);
    overflow: hidden;
  }

  .wordmark {
    position: absolute;
    font-family: "Poppins", sans-serif;
    font-weight: 600;
    white-space: nowrap;
    transform: translateX(-50%);
  }
  .wordmark--front {
    left: 392px; top: 180px;
    font-size: 66px;
    color: var(--white);
  }
  .wordmark--back {
    left: 193px; top: 205px;
    font-size: 40px;
    color: var(--purple-deep);
  }

  .motif { position: absolute; }
  .motif--watermark {
    left: 369px; top: 44px;
    width: 350px; height: 340px;
    border-radius: 50%;
    background: var(--lilac);
    opacity: .8;
  }
  .motif--trail {
    left: 164px; top: 309px;
    width: 63px; height: 110px;
    border-radius: 12px;
    background: linear-gradient(180deg, var(--purple-soft), var(--lilac));
    opacity: .6;
  }

  .ticket-info {
    position: absolute;
    left: 388px; top: 134px;
    width: 308px;
  }
  .ticket-title {
    font-family: "Fredoka", sans-serif;
    font-weight: 700;
    font-size: 27px;
    line-height: 1;
    color: var(--purple-deep);
    letter-spacing: .3px;
    text-transform: uppercase;
    white-space: nowrap;
  }
  .event-name {
    margin-top: 12px;
    font-size: 16.5px;
    color: var(--purple-mid);
    white-space: nowrap;
  }
  .write-in {
    display: flex;
    align-items: flex-end;
    font-size: 15.5px;
    font-weight: 500;
    color: var(--purple-deep);
    line-height: 1;
  }
  .write-in--date { margin-top: 56px; }
  .write-in--number { margin-top: 29px; }
  .write-in .blank {
    flex: 1;
    margin-left: 1px;
    border-bottom: 1px solid var(--purple-mid);
    height: 1px;
    margin-bottom: 1px;
  }

  .fine-print {
    position: absolute;
    left: 0; width: 778px;
    padding-left: 388px;
    padding-right: 0;
    top: 400px;
    text-align: center;
  }
  .fine-print p {
    position: absolute;
    left: 240px; width: 300px;
    font-size: 7.4px;
    font-style: italic;
    line-height: 10.5px;
    color: var(--purple-soft);
    text-align: center;
    letter-spacing: .2px;
  }
</style>
</head>
<body>
<main class="sheet">
  <h2 class="side-label side-label--front">Front</h2>

  <section class="card card--front" aria-label="Ticket front">
    <h1 class="wordmark wordmark--front">Purrline Fest</h1>
  </section>

  <section class="card card--back" aria-label="Ticket back">
    <div class="motif motif--watermark" role="img" aria-label="Large faint paw print decoration"></div>
    <div class="motif motif--trail" role="img" aria-label="Trail of small paw prints"></div>

    <p class="wordmark wordmark--back">Purrline Fest</p>

    <div class="ticket-info">
      <h3 class="ticket-title">Complimentary Ticket</h3>
      <p class="event-name">Purrline Bazaar &amp; Rescue Gala</p>
      <div class="write-in write-in--date"><span>Date:</span><span class="blank"></span></div>
      <div class="write-in write-in--number"><span>Ticket No:</span><span class="blank"></span></div>
    </div>

    <div class="fine-print">
      <p>This ticket is not redeemable for cash and cannot be combined with any other offers or discounts, can only be used for the date indicated.</p>
    </div>
  </section>

  <h2 class="side-label side-label--back">Back</h2>
</main>
</body>
</html>
```